Inpatient and outpatient services for people who have undergone urinary and faecal diversions.
Ross Halloway
Clinical Nurse Consultant Stomal Therapy
C/o K7d Surgical Unit
Corvale Hospital
Corvale 2198
P: 0412 375 804
P: 9721 3068 Pager: 41836
AS: 9721 4230 Clear writing and colour as people who read this may have vision problems
Information transfer about contact details, position of clinic, what to bring on follow up appointmants.

Target Market(s)

patients and staff to contact

Industry/Entity Type

Medical

Contact Information for Business Card

As above in Project description. Can use both sides.

Font styles to use
Decorative

Requirements
Must have
• Clear easy to read writing as patients may have eyesight problems
Nice to have
• Catchy colour & design

```html
<!DOCTYPE html>
<html lang="en">
<head>
<meta charset="utf-8">
<title>Ross Halloway – Business Card</title>
<link rel="stylesheet" href="https://fonts.googleapis.com/css2?family=Open+Sans:wght@300;400&display=swap">
<style>
  :root {
    --bg: #e9ebee;
    --card: #ffffff;
    --blue: #1a8fe3;
    --band-blue: #0a8ae6;
    --band-dark: #2b2d30;
    --ink: #1f2124;
    --rule: #8a8d92;
    --rule-light: #c9ccd0;
    --teal-1: #6fe3ec;
    --teal-2: #27bfcc;
  }
  * { box-sizing: border-box; margin: 0; padding: 0; }
  html, body { width: 1200px; height: 900px; overflow: hidden; }
  body {
    background: var(--bg);
    font-family: "Open Sans", Arial, sans-serif;
    color: var(--ink);
    position: relative;
  }
  .card {
    position: absolute;
    left: 290px;
    width: 620px;
    height: 354px;
    background: var(--card);
    box-shadow: 0 6px 18px rgba(0,0,0,.12);
    overflow: hidden;
  }
  .card--back { top: 70px; }
  .card--front { top: 476px; }

  .name {
    font-weight: 300;
    color: var(--blue);
    letter-spacing: 1.5px;
    text-transform: uppercase;
    line-height: 1;
  }
  .role {
    font-weight: 400;
    font-size: 15px;
    color: var(--ink);
    margin-top: 4px;
  }

  /* Back: appointment side */
  .back-heading {
    position: absolute;
    top: 58px;
    left: 0; right: 0;
    text-align: center;
  }
  .back-heading .name { font-size: 46px; }
  .back-heading .role { font-size: 16px; }
  .rule {
    position: absolute;
    left: 70px; right: 50px;
    height: 1px;
  }
  .rule--upper { top: 170px; background: var(--rule); }
  .rule--lower { top: 250px; background: var(--rule-light); left: 60px; }
  .appointment {
    position: absolute;
    top: 190px;
    left: 0; right: 0;
    text-align: center;
    font-size: 22px;
    font-weight: 400;
    color: var(--blue);
    letter-spacing: .5px;
  }

  /* Front: contact side */
  .front-heading {
    position: absolute;
    top: 30px;
    left: 36px;
  }
  .front-heading .name { font-size: 40px; }
  .address {
    position: absolute;
    top: 112px;
    left: 36px;
    font-size: 15px;
    line-height: 1.3;
    font-style: normal;
  }
  .contact-list {
    list-style: none;
    position: absolute;
    top: 184px;
    left: 36px;
    font-size: 15px;
    line-height: 1.3;
  }
  .contact-list .label { color: var(--blue); }
  .bands { position: absolute; left: 0; top: 0; }
  .instrument-art {
    position: absolute;
    left: 370px;
    top: 140px;
    width: 220px;
    height: 150px;
    border-radius: 48% 52% 40% 46%;
    background: radial-gradient(circle at 45% 45%, var(--teal-1), var(--teal-2));
    opacity: .85;
  }
</style>
</head>
<body>

  <section class="card card--back" aria-label="Appointment side">
    <header class="back-heading">
      <h1 class="name">Ross Halloway</h1>
      <p class="role">Clinical Nurse Consultant Stomal Therapy</p>
    </header>
    <div class="rule rule--upper"></div>
    <p class="appointment">Appointment</p>
    <div class="rule rule--lower"></div>
  </section>

  <section class="card card--front" aria-label="Contact side">
    <svg class="bands" width="620" height="354" viewBox="0 0 620 354" aria-hidden="true">
      <polygon points="0,288 214,288 200,308 0,308" fill="var(--band-dark)"/>
      <polygon points="218,300 620,300 620,336 196,336" fill="var(--band-blue)"/>
    </svg>
    <div class="instrument-art" role="img" aria-label="Teal stethoscope illustration"></div>
    <header class="front-heading">
      <h2 class="name">Ross Halloway</h2>
      <p class="role">Clinical Nurse Consultant Stomal Therapy</p>
    </header>
    <address class="address">
      C/o K7d Surgical Unit<br>
      Corvale Hospital<br>
      Corvale 2198
    </address>
    <ul class="contact-list">
      <li><span class="label">Phone:</span> 0412 375 804</li>
      <li><span class="label">Phone:</span> 9721 3068</li>
      <li><span class="label">Pager:</span> 9721 41836</li>
      <li><span class="label">AS:</span> 9721 4230</li>
    </ul>
  </section>

</body>
</html>
```